Flyer to Restuarant

This is for a new Jamaican restaurant called Mango Harbor Kitchen. It should have beach scene with coconut trees. pictures of jerk chicken, oxtails and fish platters. The Jamaican flag or The flyer should the colors of the jamaican flag. Black, green and yellow. Feel free to input own ideas.

Industry/Entity Type

Restaurant

Requirements
Must have
• It should have beach scene with coconut trees in the daytime. pictures of jerk chicken, oxtails and fish platters. The Jamaican flag or The flyer should the colors of the jamaican flag. Black, green and yellow.

```html
<!DOCTYPE html>
<html lang="en">
<head>
<meta charset="utf-8">
<title>Mango Harbor Kitchen – Flyer</title>
<link rel="stylesheet" href="https://fonts.googleapis.com/css2?family=Arimo:wght@400;700&display=swap">
<style>
  :root {
    --page-bg: #e9e6e1;
    --flyer-black: #060606;
    --brand-green: #7cc242;
    --brand-yellow: #eee812;
    --body-green: #6fb33a;
    --band-grey: #3a3a3a;
    --oval-white: #ffffff;
    --ink-black: #0b0b0b;
  }
  * { box-sizing: border-box; margin: 0; padding: 0; }
  html, body {
    width: 1200px; height: 900px; overflow: hidden;
    background: var(--page-bg);
    font-family: "Arimo", Arial, sans-serif;
  }
  .flyer {
    position: absolute; left: 300px; top: 30px;
    width: 600px; height: 840px;
    background: var(--flyer-black);
    overflow: hidden;
    box-shadow: 0 6px 24px rgba(0,0,0,.25);
  }
  .flyer-shapes { position: absolute; inset: 0; width: 600px; height: 840px; }
  .brand-name {
    position: absolute; left: 392px; top: 160px; width: 200px;
    color: var(--brand-green); font-weight: 700; font-size: 23px;
    line-height: 1.1; text-transform: uppercase; text-align: center;
  }
  .headline {
    position: absolute; left: 40px; top: 385px; width: 300px;
    color: var(--brand-yellow); font-weight: 700; font-size: 25px;
    line-height: 1.15; text-align: center;
  }
  .body-copy {
    position: absolute; left: 40px; top: 452px; width: 290px;
    color: var(--body-green); font-size: 12.5px; line-height: 1.45;
  }
  .accent-square {
    position: absolute; left: 22px; top: 630px; width: 36px; height: 26px;
    background: linear-gradient(90deg, var(--brand-green) 0 40%, var(--brand-yellow) 40% 100%);
  }
  .dish {
    position: absolute; border: 3px solid #fff; border-radius: 10px;
  }
  .dish-oxtail { left: 350px; top: 392px; width: 140px; height: 95px;
    background: radial-gradient(circle at 50% 55%, #5a2d15, #8a4a22 45%, #e8ddd0 75%); }
  .dish-jerk { left: 498px; top: 450px; width: 96px; height: 112px;
    background: radial-gradient(circle at 50% 55%, #b85d20, #7a3f14 45%, #3b2610 80%); }
  .dish-fish { left: 350px; top: 505px; width: 140px; height: 105px;
    background: radial-gradient(circle at 50% 50%, #c99a62, #d9412f 40%, #5e8c3a 65%, #f1efe8 85%); }
  .contact {
    position: absolute; left: 265px; top: 740px; width: 330px;
    color: var(--ink-black); font-weight: 700; font-size: 22px; line-height: 1.45;
  }
</style>
</head>
<body>
  <main class="flyer">
    <svg class="flyer-shapes" viewBox="0 0 600 840" aria-hidden="true">
      <defs>
        <linearGradient id="beach-tones" x1="0" y1="0" x2="1" y2="1">
          <stop offset="0" stop-color="#4f7a45"/>
          <stop offset="0.35" stop-color="#7fb4dc"/>
          <stop offset="0.6" stop-color="#9fd1e6"/>
          <stop offset="0.75" stop-color="#3fb6c4"/>
          <stop offset="1" stop-color="#e6dccb"/>
        </linearGradient>
      </defs>
      <g fill="none">
        <path d="M160 0 C150 120 160 200 200 240 C240 280 300 290 330 310 C355 330 370 345 420 350 C480 355 540 350 600 350"
              stroke="var(--brand-yellow)" stroke-width="58"/>
        <path d="M160 0 C150 120 160 200 200 240 C240 280 300 290 330 310 C355 330 370 345 420 350 C480 355 540 350 600 350"
              stroke="var(--flyer-black)" stroke-width="38"/>
        <path d="M160 0 C150 120 160 200 200 240 C240 280 300 290 330 310 C355 330 370 345 420 350 C480 355 540 350 600 350"
              stroke="var(--brand-green)" stroke-width="22"/>
      </g>
      <path d="M160 0 C150 120 160 200 200 240 C240 280 300 290 330 310 C355 330 370 345 420 350 C480 355 540 350 600 350 V0 Z"
            fill="url(#beach-tones)" role="img" aria-label="Daytime beach with coconut palm trees, sand and turquoise sea"/>
      <ellipse cx="520" cy="185" rx="135" ry="82" fill="var(--oval-white)"/>
      <path d="M190 840 V740 C190 640 300 610 420 630 L600 660 V840 Z" fill="var(--band-grey)"/>
      <path d="M210 840 V748 C210 665 300 640 420 655 L600 682 V840 Z" fill="var(--brand-green)"/>
      <path d="M235 840 V755 C235 685 310 668 420 680 L600 704 V840 Z" fill="var(--brand-yellow)"/>
    </svg>

    <h1 class="brand-name">Mango Harbor<br>Kitchen</h1>
    <h2 class="headline">Your Beutiful Headline<br>Goes Here</h2>
    <p class="body-copy">Lorem Ipsum is simply dummy text of the printing and typesetting industry. Lorem Ipsum has been the industry's standard dummy text ever since the 1500s, when an unknown printer took a galley of type and scrambled it to make a type specimen book. It has survived not only five centuries, but also the leap into electronic typesetting, remaining essentially unchanged.</p>
    <div class="accent-square"></div>

    <div class="dish dish-oxtail" role="img" aria-label="Plate of braised oxtails"></div>
    <div class="dish dish-jerk" role="img" aria-label="Jerk chicken"></div>
    <div class="dish dish-fish" role="img" aria-label="Fish platter with fresh salad"></div>

    <p class="contact">Contact Us : 000-0000-000<br>www.yoursitename.com</p>
  </main>
</body>
</html>
```